"KTR Community Supports" Business Card Design

We are a not for profit disability service that has recently changed its logo and trading name and is in the process of "rebranding".We provide employment, training and accommodation to people with disabilities. We find our new logo fresh and inspiring and would like our new business cards to reflect the same feeling. Our marketing line is "Growth, Opportunity, Empowerment".

Target Market(s)

People with disabilities and their families, carers, support network

Industry/Entity Type

Business

Contact Information for Business Card

Requirements
Must have
• Our logo; space for the above listed information requirements

```html
<!DOCTYPE html>
<html lang="en">
<head>
<meta charset="utf-8">
<title>KTR Community Supports – Business Card</title>
<link rel="stylesheet" href="https://fonts.googleapis.com/css2?family=Open+Sans:wght@400;600;700&display=swap">
<style>
  :root {
    --canvas: #e4e5e6;
    --paper: #ffffff;
    --navy: #0d3f7e;
    --blue: #1269b0;
    --green: #7cb342;
    --ink-light: #ffffff;
    --shadow: rgba(0, 0, 0, 0.18);
  }
  * { box-sizing: border-box; margin: 0; padding: 0; }
  html, body {
    width: 1200px;
    height: 772px;
    overflow: hidden;
    background: var(--canvas);
    font-family: "Open Sans", Arial, sans-serif;
  }
  .card-sheet {
    position: relative;
    width: 1200px;
    height: 772px;
  }
  .card {
    position: absolute;
    top: 236px;
    width: 525px;
    height: 300px;
    background: var(--paper);
    box-shadow: 0 6px 18px var(--shadow);
    overflow: hidden;
  }
  .card--front { left: 60px; }
  .card--back  { left: 615px; }

  .brand {
    display: flex;
    align-items: center;
    gap: 12px;
    color: var(--navy);
    font-weight: 700;
    white-space: nowrap;
  }
  .brand__dot {
    flex: none;
    border-radius: 50%;
    background: var(--green);
  }
  .card--front .brand {
    position: absolute;
    left: 50%;
    top: 50%;
    transform: translate(-50%, -50%);
    font-size: 30px;
  }
  .card--front .brand__dot { width: 34px; height: 34px; }

  .card--back .brand {
    position: absolute;
    left: 26px;
    top: 26px;
    font-size: 17px;
    gap: 8px;
  }
  .card--back .brand__dot { width: 20px; height: 20px; }

  .wave {
    position: absolute;
    inset: 0;
    width: 525px;
    height: 300px;
  }

  .contact {
    position: absolute;
    right: 26px;
    bottom: 22px;
    text-align: right;
    color: var(--ink-light);
  }
  .contact__name {
    font-size: 15px;
    font-weight: 600;
    letter-spacing: 1px;
    text-transform: uppercase;
  }
  .contact__role {
    font-size: 11px;
    margin-bottom: 12px;
    opacity: 0.9;
  }
  .contact__line {
    display: flex;
    justify-content: flex-end;
    align-items: center;
    gap: 8px;
    font-size: 11px;
    line-height: 19px;
  }
  .contact__address { font-size: 11px; line-height: 16px; margin-bottom: 8px; }
  .icon { width: 11px; height: 11px; flex: none; }
</style>
</head>
<body>
<main class="card-sheet">

  <section class="card card--front" aria-label="Business card front">
    <div class="brand">
      <span class="brand__dot"></span>
      <span class="brand__name">KTR Community Supports</span>
    </div>
  </section>

  <section class="card card--back" aria-label="Business card back">
    <svg class="wave" viewBox="0 0 525 300" aria-hidden="true">
      <defs>
        <linearGradient id="blueField" x1="0" y1="0" x2="1" y2="1">
          <stop offset="0" stop-color="#0a3a72"/>
          <stop offset="0.5" stop-color="#1a78c2"/>
          <stop offset="1" stop-color="#0d4d92"/>
        </linearGradient>
        <linearGradient id="greenBand" x1="0" y1="0" x2="1" y2="0">
          <stop offset="0" stop-color="#4f8a2a"/>
          <stop offset="1" stop-color="#9ccc65"/>
        </linearGradient>
      </defs>
      <path d="M0 106 C170 96 250 36 525 16 L525 32 C262 54 180 114 0 122 Z" fill="url(#greenBand)"/>
      <path d="M0 132 C180 124 262 62 525 42 L525 300 L0 300 Z" fill="url(#blueField)"/>
    </svg>

    <div class="brand">
      <span class="brand__dot"></span>
      <span class="brand__name">KTR Community Supports</span>
    </div>

    <div class="contact">
      <p class="contact__name">Daniel Marsh</p>
      <p class="contact__role">Managing Director</p>
      <p class="contact__address">14 Fern Street,<br>Riverside Park</p>
      <p class="contact__line">021 555 0148
        <svg class="icon" viewBox="0 0 12 12" aria-hidden="true"><path d="M2 1h3l1 3-2 1a7 7 0 0 0 3 3l1-2 3 1v3c-5 0-9-4-9-9z" fill="#fff"/></svg>
      </p>
      <p class="contact__line">021 555 0149
        <svg class="icon" viewBox="0 0 12 12" aria-hidden="true"><rect x="3" y="1" width="6" height="10" rx="1" fill="none" stroke="#fff" stroke-width="1.4"/></svg>
      </p>
      <p class="contact__line">mail@ktrsupports.org
        <svg class="icon" viewBox="0 0 12 12" aria-hidden="true"><rect x="1" y="2.5" width="10" height="7" fill="none" stroke="#fff" stroke-width="1.2"/><path d="M1 3l5 4 5-4" fill="none" stroke="#fff" stroke-width="1.2"/></svg>
      </p>
      <p class="contact__line">www.ktrsupports.org
        <svg class="icon" viewBox="0 0 12 12" aria-hidden="true"><circle cx="6" cy="6" r="5" fill="none" stroke="#fff" stroke-width="1.2"/><path d="M1 6h10M6 1c-3 3-3 7 0 10M6 1c3 3 3 7 0 10" fill="none" stroke="#fff" stroke-width="1"/></svg>
      </p>
    </div>
  </section>

</main>
</body>
</html>
```